New professional looking flyer for company

I need our flyer updated my flyer is the Lvb flyer Have attached current flyer so you know what services need to be listed. Want it to be in mainly dark colours like black and dark grey with pops of light grey, silver or white. i have added several photos for you to choose which ones work best with your design would like The photos to be in colour for the flyer. But can have a mix of greyscale if that works for your design j have attached another companies flyers as design ideas to show what I am looking for

Target Market(s)

new clients

Industry/Entity Type

transport and earthmoving

Colors

Designer to choose colors to be used in the design.

Requirements
Nice to have
• Look professional
Should not have
• No orange or red or green

```html
<!DOCTYPE html>
<html lang="en">
<head>
<meta charset="utf-8">
<title>LVB Pty Ltd – Services Flyer</title>
<link href="https://fonts.googleapis.com/css2?family=Teko:wght@400;500;600&family=Quicksand:wght@500;600&family=Montserrat:wght@400;600&display=swap" rel="stylesheet">
<style>
  :root{
    --page:#ececec;
    --ink:#1b1917;
    --panel-grey:#9c9c9c;
    --silver:#c9c9c9;
    --white:#ffffff;
    --gold:#7b5d26;
    --gold-text:#8a6a2e;
    --muted:#a8a8a8;
  }
  *{margin:0;padding:0;box-sizing:border-box}
  html,body{width:1200px;height:2614px;overflow:hidden;background:var(--page)}
  .flyer{position:absolute;left:50px;top:530px;width:1100px;height:1553px;background:var(--ink);overflow:hidden}
  .header{position:absolute;left:0;top:0;width:1100px;height:180px;
    background:radial-gradient(ellipse at 50% 55%,#3c3c3c 0%,#1a1a1a 55%,#0e0e0e 100%)}
  .hero-photo{position:absolute;left:0;top:179px;width:1100px;height:282px;
    background:
      linear-gradient(180deg,rgba(20,18,16,.0) 0%,rgba(20,18,16,.0) 100%),
      linear-gradient(180deg,#1c1a18 0%,#2e2a26 28%,#3a3630 44%,#6e4a30 58%,#a8693c 76%,#8a5430 100%)}
  .brand-lockup{position:absolute;left:0;top:22px;width:1100px;display:flex;justify-content:center;align-items:flex-end;gap:14px}
  .brand{font-family:'Teko',sans-serif;font-weight:600;font-size:190px;line-height:150px;color:var(--silver);letter-spacing:10px}
  .brand-suffix{font-family:'Montserrat',sans-serif;font-weight:600;font-size:28px;line-height:28px;color:var(--muted);margin-bottom:16px}
  .services-bg{position:absolute;left:0;top:461px;width:1100px;height:844px;
    background:linear-gradient(90deg,#1d1b19 0%,#2b2622 55%,#1d1b19 100%)}
  .photo-panel{position:absolute;left:53px;top:425px;width:448px;height:880px;background:var(--panel-grey)}
  .photo{position:absolute;left:70px;width:415px;height:270px}
  .photo-1{top:436px;background:linear-gradient(180deg,#7594b4 0%,#a9b6c2 30%,#8c8a84 52%,#5a5752 75%,#3e3c3a 100%)}
  .photo-2{top:724px;background:linear-gradient(180deg,#3f6fb4 0%,#7ea0c8 30%,#b39a78 48%,#c99a62 70%,#b67e48 100%)}
  .photo-3{top:1014px;background:linear-gradient(180deg,#4a5660 0%,#5c6064 30%,#7a665c 50%,#9a6248 75%,#8c543c 100%)}
  .services-title{position:absolute;left:534px;top:500px;font-family:'Teko',sans-serif;font-weight:600;
    font-style:italic;font-size:76px;line-height:76px;color:var(--white);letter-spacing:2px}
  .services-rule{position:absolute;left:534px;top:576px;width:391px;height:3px;background:var(--white)}
  .services-list{position:absolute;left:540px;top:600px;list-style:none}
  .services-list li{font-family:'Teko',sans-serif;font-weight:500;font-size:40px;line-height:53.8px;
    color:var(--white);padding-left:30px;position:relative;white-space:nowrap}
  .services-list li::before{content:"";position:absolute;left:0;top:20px;width:18px;height:18px;
    border-radius:50%;background:var(--white)}
  .services-list li.two-line{line-height:43px;padding-top:5px}
  .truck-photo{position:absolute;left:872px;top:1109px;width:226px;height:190px;
    background:linear-gradient(180deg,rgba(40,40,44,0) 0%,#34343a 30%,#3c3c40 60%,#6a4a30 100%)}
  .callout{position:absolute;left:0;top:1305px;width:1100px;height:103px;background:var(--white);text-align:center}
  .callout-lead{font-family:'Quicksand',sans-serif;font-weight:600;font-size:31px;color:var(--ink);margin-top:10px;line-height:36px}
  .callout-cta{font-family:'Teko',sans-serif;font-weight:500;font-size:44px;color:var(--gold-text);line-height:48px}
  .footer-strip{position:absolute;left:53px;top:1408px;width:448px;height:25px;background:var(--silver)}
  .address-bar{position:absolute;left:551px;top:1408px;width:549px;height:46px;background:var(--gold)}
  .contact{position:absolute;display:flex;align-items:center;gap:14px;font-family:'Montserrat',sans-serif;color:var(--white)}
  .contact svg{flex:none}
  .contact-address{left:578px;top:1408px;height:46px;font-size:28px}
  .contact-email{left:578px;top:1460px;height:46px;font-size:28px}
  .contact-phone{left:110px;top:1446px;height:46px;font-size:36px;font-weight:600}
</style>
</head>
<body>
<main class="flyer">
  <div class="header"></div>
  <div class="hero-photo" role="img" aria-label="Road train with three side-tipper trailers on red outback dirt"></div>
  <div class="brand-lockup">
    <span class="brand">LVB</span>
    <span class="brand-suffix">Pty Ltd</span>
  </div>

  <div class="services-bg"></div>
  <div class="photo-panel"></div>
  <div class="photo photo-1" role="img" aria-label="Prime mover hauling a grader on a low loader, oversize load"></div>
  <div class="photo photo-2" role="img" aria-label="Wheel loader on a drop deck trailer behind a white truck"></div>
  <div class="photo photo-3" role="img" aria-label="Two trucks with a loader on a float parked on red ground"></div>

  <h2 class="services-title">OUR SERVICES</h2>
  <div class="services-rule"></div>
  <ul class="services-list">
    <li>Over size loads / Hot Shot Loads</li>
    <li>HeavyVehicle Recovery Services</li>
    <li>PotableWaterDeliveries</li>
    <li>RoadBuilding / Maintenance</li>
    <li>Earthworks</li>
    <li>Sand &amp; Metal Supply &amp; Cartage</li>
    <li>Road Train Tippers</li>
    <li>Road Train Tankers</li>
    <li>Road Train Flat Tops</li>
    <li>Drop Deck Trailers</li>
    <li class="two-line">Mine Site accreditede<br>quipment &amp; Operators</li>
  </ul>
  <div class="truck-photo" role="img" aria-label="Black road train prime mover with oversize sign"></div>

  <section class="callout">
    <p class="callout-lead">We offer a large range of services not listed so</p>
    <p class="callout-cta">CALL US TODAY FOR A PERSONALISED QUOTE TO SUIT YOUR NEEDS</p>
  </section>

  <div class="footer-strip"></div>
  <div class="address-bar"></div>
  <div class="contact contact-address">
    <svg width="26" height="30" viewBox="0 0 26 30" fill="none" stroke="#fff" stroke-width="2.2"><path d="M13 28C13 28 4 18 4 11a9 9 0 0 1 18 0c0 7-9 17-9 17z"/><circle cx="13" cy="11" r="3.5"/></svg>
    <span>your office address here</span>
  </div>
  <div class="contact contact-email">
    <svg width="28" height="20" viewBox="0 0 28 20" fill="none" stroke="#fff" stroke-width="2.2"><rect x="1.5" y="1.5" width="25" height="17"/><path d="M1.5 1.5l12.5 10 12.5-10M1.5 18.5l9-8M26.5 18.5l-9-8"/></svg>
    <span>info@lvb.com.au</span>
  </div>
  <div class="contact contact-phone">
    <svg width="26" height="40" viewBox="0 0 26 40" fill="none" stroke="#fff" stroke-width="2.4"><rect x="2" y="2" width="22" height="36" rx="4"/><path d="M8 33h10"/><path d="M9 12c0 6 3 11 8 13l2-3-3-2-2 1c-2-1-3-3-3-5l1-2-2-3z" fill="#fff" stroke="none"/></svg>
    <span>+123 456 789</span>
  </div>
</main>
</body>
</html>
```